Flight Medical Brochure

Skyvale Care Transit is a flight medical company that provides worldwide transportation for sick and injured people. We are marketing ourselves to hospital social workers who generally arrange transportation for patients in the hospital. The brochure needs to grab their attention, and build confidence that we are professional and competent. We have written sample copy below:

"When you need medical relocation or repatriation services for your patients, Skyvale Care Transit is the only number that you need to call. Whether your patient needs to go across the country or across the world, we can help. From start to finish our professional staff will be there to make the process fast and simple.

Why choose Skyvale Care Transit?

Comprehensive Service:
• Our staff can assist with every step of the process, from helping to find accepting physicians and hospitals to coordinating with embassies and consulates; we can make the complex simple.
• We coordinate travel from beside to bedside, including ground transport, airline ticketing, medical clearances and more.
• Whether your patient needs a single paramedic or a full medical team, our experienced providers can handle virtually any patient.

Speed:
• In most cases, transports can be arranged in under 48 hours when all necessary details are in order.
• Our experience and familiarity with the process helps you to avoid costly delays and missed details.

Competence:
• Our flight paramedics and flight nurses have worked in dozens of countries on every continent including out of the way places such as Micronesia and Uzbekistan.
• Every member of our flight staff has years of emergency and/or critical care experience.
• All logistics are handled in-house ensuring every detail is taken care of.

For more information, or to arrange a flight, call us at 888-416-2097 or visit our website at www.skyvalecaretransit.example. "
Updates

Reason: We have received some great designs. We are waiting on several revisions and wanted to make sure everyone had enough time to get their best design in. Thanks for everyone's hard work!

Sorry everyone for the delay.  My partners left me in charge of this and I was in the Dominican Republic on Thursday, Montreal on Friday, Toronto on Saturday and got back last night.  It was a challenge choosing a design, as there were several really good ones submitted.  Thanks everyone for working hard and giving us such great options to choose from.  Good luck to everyone!

Target Market(s)

Nurse case managers and social workers in hospitals

Industry/Entity Type

Marketing

Requirements
Must have
• The brochure needs to grab the attention, and great photos would be a plus. As most of our patients are transported by commercial aircraft, airport/airplane related photos may work well.

I have attached our logo in various file formats. It should feature prominently in the brochure. Also, our phone number 1-888-416-2097 and website www.skyvalecaretransit.example should be highly visible.
Should not have
• Please avoid cartoonish or childish graphics. This should look professional.

```html
<!DOCTYPE html>
<html lang="en">
<head>
<meta charset="utf-8">
<title>Skyvale Care Transit – Trifold Brochure</title>
<link href="https://fonts.googleapis.com/css2?family=Arimo:wght@400;700&family=Open+Sans:wght@300;400&family=Spectral:wght@400&display=swap" rel="stylesheet">
<style>
  :root{
    --page-bg:#ece8e2;
    --brand-blue:#2f86c9;
    --brand-blue-dark:#1f6aa6;
    --panel-light:#ececec;
    --panel-dark:#a8a8a8;
    --ink:#1d1d1d;
    --ink-soft:#333;
    --alert-red:#d3252b;
    --white:#ffffff;
  }
  *{box-sizing:border-box;margin:0;padding:0}
  html,body{width:1200px;height:900px;overflow:hidden}
  body{background:var(--page-bg);font-family:"Arimo",Arial,sans-serif;color:var(--ink);position:relative}

  .spread-label{position:absolute;font-family:"Spectral",Georgia,serif;font-size:40px;color:#222;letter-spacing:.5px}
  .spread-label--inside{left:250px;top:510px}
  .spread-label--outside{left:830px;top:320px}

  .brochure{position:absolute;width:558px;height:433px;background:linear-gradient(180deg,var(--panel-light),var(--panel-dark));box-shadow:0 6px 18px rgba(0,0,0,.25);overflow:hidden}
  .brochure--inside{left:40px;top:50px}
  .brochure--outside{left:600px;top:400px}
  .fold{position:absolute;top:0;bottom:0;width:1px;background:rgba(0,0,0,.18)}
  .fold--a{left:186px}.fold--b{left:372px}

  .block{position:absolute}
  .photo{position:absolute}
  .band{position:absolute;background:var(--brand-blue)}

  .panel-title{position:absolute;font-family:"Open Sans",Arial,sans-serif;font-weight:300;color:var(--white);font-size:20px;line-height:1.2}

  .copy{position:absolute;font-size:8.4px;line-height:1.32;color:var(--ink-soft)}
  .copy h3{font-size:10px;font-weight:700;color:var(--ink);margin-bottom:7px}
  .copy ul{list-style:none}
  .copy li{margin-bottom:7px;padding-left:7px;text-indent:-7px}
  .copy li::before{content:"• "}
  .copy p{margin-bottom:6px}

  .wordmark{position:absolute;display:flex;align-items:center;gap:6px}
  .wordmark__dot{width:22px;height:22px;border-radius:50%;background:var(--brand-blue);flex:none}
  .wordmark__name{font-weight:700;color:#111;font-size:12px;line-height:1.05}
  .wordmark--large .wordmark__dot{width:34px;height:34px}
  .wordmark--large .wordmark__name{font-size:19px}

  .tag{position:absolute;background:var(--alert-red);color:var(--white);font-size:10px;padding:3px 7px}
  .cover-title{position:absolute;color:var(--white);font-size:15px;text-align:center;line-height:1.25}
  .contact-note{position:absolute;color:var(--white);font-size:7.4px;line-height:1.35}
  .web-bar{position:absolute;background:var(--brand-blue);color:var(--white);font-size:9px;padding:5px 10px;text-align:right}
</style>
</head>
<body>

<div class="spread-label spread-label--inside">Inside Pages</div>
<div class="spread-label spread-label--outside">Outside Pages</div>

<!-- Inside spread -->
<section class="brochure brochure--inside" aria-label="Inside pages">
  <div class="band" style="left:0;top:0;width:186px;height:95px"></div>
  <h2 class="panel-title" style="left:12px;top:22px;width:165px">Why choose Skyvale Care Transit?</h2>
  <div class="photo" role="img" aria-label="Close-up of a stethoscope on a medical chart" style="left:0;top:95px;width:186px;height:90px;background:linear-gradient(135deg,#d9dcdf,#8c969e 55%,#b63a44)"></div>
  <div class="copy" style="left:12px;top:198px;width:164px">
    <h3>Comprehensive Service:</h3>
    <ul>
      <li>Our staff can assist with every step of the process, from helping to find accepting physicians and hospitals to coordinating with embassies and consulates; we can make the complex simple.</li>
      <li>We coordinate travel from beside to bedside, including ground transport, airline ticketing, medical clearances and more.</li>
      <li>Whether your patient needs a single paramedic or a full medical team, our experienced providers can handle virtually any patient.</li>
    </ul>
  </div>

  <div class="band" style="left:186px;top:0;width:372px;height:62px"></div>
  <div class="wordmark" style="left:200px;top:20px">
    <span class="wordmark__dot"></span>
    <span class="wordmark__name">Skyvale Care Transit</span>
  </div>
  <div class="photo" role="img" aria-label="Passenger jet flying past snowy mountain peaks" style="left:186px;top:62px;width:372px;height:72px;background:linear-gradient(180deg,#9fb1c6,#d7dde3 60%,#8e98a3)"></div>

  <div class="copy" style="left:198px;top:148px;width:164px">
    <h3>Speed:</h3>
    <ul>
      <li>In most cases, transports can be arranged in under 48 hours when all necessary details are in order.</li>
      <li>Our experience and familiarity with the process helps you to avoid costly delays and missed details.</li>
    </ul>
  </div>
  <div class="copy" style="left:384px;top:148px;width:164px">
    <h3>Competence:</h3>
    <ul>
      <li>Our flight paramedics and flight nurses have worked in dozens of countries on every continent including out of the way places such as Micronesia and Uzbekistan.</li>
      <li>Every member of our flight staff has years of emergency and/or critical care experience.</li>
      <li>All logistics are handled in-house ensuring every detail is taken care of.</li>
    </ul>
  </div>
  <div class="photo" role="img" aria-label="Medical helicopter on a hospital rooftop helipad with a flight nurse in scrubs" style="left:186px;top:318px;width:372px;height:115px;background:linear-gradient(180deg,#b9c7d6,#7d8a7a 55%,#5f6d5a)"></div>

  <div class="fold fold--a"></div><div class="fold fold--b"></div>
</section>

<!-- Outside spread -->
<section class="brochure brochure--outside" aria-label="Outside pages">
  <div class="photo" role="img" aria-label="Flight crew loading a patient on a stretcher into an aircraft" style="left:0;top:0;width:186px;height:205px;background:linear-gradient(160deg,#5b6a7c,#2f3a48 50%,#a58a3a)"></div>
  <div class="tag" style="left:8px;top:195px">About Skyvale Care Transit</div>
  <div class="copy" style="left:12px;top:228px;width:164px">
    <p>Skyvale Care Transit is a leader in domestic and international medical repatriation.</p>
    <p>We arrange transport and provide professional medical staff to accompany patients to or from almost anywhere in the world. Skyvale Care Transit provides first-class, compassionate care that is always focused on the client. We offer solutions for a wide range of clients including hospitals, families, corporations and many more.</p>
  </div>

  <div class="band" style="left:186px;top:0;width:372px;height:62px"></div>
  <p class="contact-note" style="left:198px;top:12px;width:164px">For more information, or to arrange a flight, call us at 888-416-2097 or visit our website at www.skyvalecaretransit.example</p>
  <div class="photo" role="img" aria-label="Medical team wheeling a patient on a stretcher toward a helicopter on the tarmac" style="left:186px;top:62px;width:372px;height:200px;background:linear-gradient(180deg,#c9d3dc,#8a939b 55%,#4d555c)"></div>
  <div class="band" style="left:372px;top:0;width:186px;height:92px"></div>
  <h1 class="cover-title" style="left:372px;top:28px;width:186px">Skyvale Care Transit</h1>

  <div class="copy" style="left:198px;top:278px;width:164px">
    <p>When you need medical relocation or repatriation services for your patients, Skyvale Care Transit is the only number that you need to call. Whether your patient needs to go across the country or across the world, we can help. From start to finish our professional staff will be there to make the process fast and simple.</p>
  </div>
  <div class="wordmark" style="left:206px;top:378px">
    <span class="wordmark__dot"></span>
    <span class="wordmark__name">Skyvale Care Transit</span>
  </div>

  <div class="wordmark wordmark--large" style="left:384px;top:300px;width:166px">
    <span class="wordmark__dot"></span>
    <span class="wordmark__name">Skyvale Care Transit</span>
  </div>
  <div class="web-bar" style="left:372px;top:396px;width:186px">www.skyvalecaretransit.example</div>

  <div class="fold fold--a"></div><div class="fold fold--b"></div>
</section>

</body>
</html>
```